Design my New and Engaging Wix Website

We just recently started a new website for Harbor Lumen (www.harbor-lumen.example) and would like to have a custom design for it. The design should be engaging and modern. You can use our logo and design the website inspired by the style.

```html
<!DOCTYPE html>
<html lang="en">
<head>
<meta charset="utf-8">
<title>Harbor Lumen – Peace Education Resources</title>
<link href="https://fonts.googleapis.com/css2?family=Rubik:wght@400;500&display=swap" rel="stylesheet">
<style>
:root{
  --blue:#0a93e0;
  --blue-dark:#0a6fc2;
  --ink:#1b1b1b;
  --white:#ffffff;
  --pale:#e6f3fc;
  --gray-bg:#f7f7f7;
  --hero-b:#6b5a3f;
}
*{box-sizing:border-box;margin:0;padding:0}
html,body{width:1200px;height:2765px;overflow:hidden}
body{font-family:"Rubik",sans-serif;color:var(--ink);background:var(--white);position:relative}
.abs{position:absolute}
a{color:inherit;text-decoration:none}

.site-header{position:absolute;left:0;top:0;width:1200px;height:80px;background:var(--white)}
.brand{position:absolute;left:88px;top:22px;display:flex;align-items:center;gap:10px;color:var(--blue);font-size:30px;font-weight:400}
.brand-dot{width:26px;height:26px;border:3px solid var(--blue);border-radius:50%}
.nav{position:absolute;top:30px;font-size:14px}
.nav.active{color:var(--blue);text-decoration:underline}
.btn-inquiry{position:absolute;left:966px;top:21px;width:146px;height:37px;border:2px solid var(--blue);border-radius:3px;color:var(--blue);font-size:15px;font-weight:500;display:flex;align-items:center;justify-content:center}

.hero{position:absolute;left:0;top:80px;width:1200px;height:464px;background:linear-gradient(100deg,#1f1f22 0%,#3a3430 45%,var(--hero-b) 75%,#3a3126 100%)}
.hero h1{position:absolute;left:92px;top:102px;white-space:nowrap;color:var(--white);font-size:37px;line-height:48px;font-weight:500}
.hero .tagline{position:absolute;left:92px;top:258px;color:var(--blue);font-size:19px;font-weight:500}
.btn-primary{position:absolute;background:var(--blue);color:var(--white);font-size:16px;font-weight:500;border-radius:3px;display:flex;align-items:center;justify-content:center}
.hero-dots{position:absolute;left:1092px;top:206px}
.hero-dots span{display:block;width:12px;height:12px;border:1px solid #bbb;border-radius:50%;margin-bottom:8px}
.hero-dots span.on{border-color:var(--blue);background:radial-gradient(circle,var(--blue) 40%,transparent 45%)}

.about{position:absolute;left:0;top:544px;width:1200px;height:542px}
.about-photo{position:absolute;left:114px;top:90px;width:370px;height:370px;border-radius:50%;background:radial-gradient(circle at 55% 40%,#d8c7a4,#8c8a62 60%,#5f6c48)}
.about-ring{position:absolute;left:104px;top:80px;width:390px;height:390px;border:2px solid var(--blue);border-radius:50%}
.about h2{position:absolute;left:554px;top:90px;color:var(--blue);font-size:33px;font-weight:500}
.about .copy{position:absolute;left:554px;top:148px;width:530px;font-size:14px;line-height:21px}
.about .copy p{margin-bottom:21px}
.btn-outline{position:absolute;border:1px solid var(--ink);border-radius:3px;font-size:14px;display:flex;align-items:center;justify-content:center;background:var(--white)}

.services{position:absolute;left:0;top:1086px;width:1200px;height:586px;background:var(--blue)}
.services h2{position:absolute;left:0;width:1200px;top:72px;text-align:center;color:var(--white);font-size:33px;font-weight:500}
.svc-img{position:absolute;width:325px;height:232px;border-radius:3px}
.svc-card{position:absolute;width:297px;height:183px;background:var(--white);box-shadow:0 2px 6px rgba(0,0,0,.15);padding:20px 22px}
.svc-card h3{color:var(--blue);font-size:19px;font-weight:500;line-height:24px}
.svc-card p{font-size:14px;line-height:18px;margin-top:10px}

.video-band{position:absolute;left:0;top:1672px;width:1200px;height:395px;background:linear-gradient(180deg,#3a2e22,#5a4a35 60%,#4a3c2a)}
.video-under{position:absolute;left:0;top:2067px;width:1200px;height:168px;background:var(--gray-bg)}
.video-frame{position:absolute;left:251px;top:1768px;width:698px;height:387px;background:linear-gradient(180deg,#5d8f34,#4f8029 75%,#3c6120)}

.consortium h2{position:absolute;left:90px;width:600px;top:2305px;text-align:center;color:var(--blue);font-size:33px;font-weight:500}
.consortium .sub{position:absolute;left:90px;width:600px;top:2347px;text-align:center;color:var(--blue);font-size:16px}
.partner{position:absolute;top:2402px;width:289px;height:174px;border:1px solid #e3e3e3;border-radius:6px;display:flex;align-items:center;justify-content:center;gap:10px;font-size:19px;font-weight:500;color:#1f3b7a;text-align:left;line-height:22px}
.partner-mark{width:56px;height:56px;border-radius:50%;background:#2c4a8c;flex:none}
.partner-cap{position:absolute;top:2596px;width:289px;text-align:center;font-size:15px;line-height:20px;font-weight:500;text-transform:uppercase}

.donor{position:absolute;left:775px;top:2314px;width:337px;height:328px;background:var(--pale)}
.donor h2{text-align:center;color:var(--blue);font-size:33px;font-weight:500;margin-top:20px}
.donor-card{position:absolute;left:28px;top:70px;width:281px;height:237px;background:var(--white);border-radius:12px;display:flex;flex-direction:column;align-items:center;justify-content:center;gap:12px}
.donor-mark{width:140px;height:140px;border-radius:50%;background:var(--blue-dark)}
.donor-name{font-size:14px;color:var(--ink)}

.site-footer{position:absolute;left:0;top:2723px;width:1200px;height:42px;background:var(--blue);color:var(--white);font-size:14px;display:flex;align-items:center;justify-content:center}
</style>
</head>
<body>

<header class="site-header">
  <div class="brand"><span class="brand-dot"></span>Harbor Lumen</div>
  <a class="nav active" style="left:589px">Home</a>
  <a class="nav" style="left:663px">About Us</a>
  <a class="nav" style="left:758px">Services</a>
  <a class="nav" style="left:849px">Contact Us</a>
  <a class="btn-inquiry">Quick Inquiry</a>
</header>

<section class="hero" role="img" aria-label="Photo of students in a lecture hall">
  <h1>QUALITATIVE AND<br>ACCESSIBLE PEACE<br>EDUCATION RESOURCES</h1>
  <div class="tagline">Our Mission and Contribution</div>
  <a class="btn-primary" style="left:92px;top:306px;width:144px;height:40px">Contact Us</a>
  <div class="hero-dots"><span></span><span class="on"></span><span></span></div>
</section>

<section class="about">
  <div class="about-ring"></div>
  <div class="about-photo" role="img" aria-label="Photo of two women studying together with a tablet"></div>
  <h2>About Us</h2>
  <div class="copy">
    <p>In an increasingly internationalized world, complex and manifold conflicts arise between individuals, groups, organizations, and states.</p>
    <p>To find ways of dealing with these issues in a constructive and peaceful manner is a central challenge for modern societies. Harbor Lumen aims to empower communities affected by unresolved conflicts and strengthen their capacities to address them effectively.</p>
    <p>Within our pilot project "Digital Bridges for Learning in Ukraine" the Northvale University Arden (NUA) in cooperation with the Eastmere National Academy (ENA) uses means of</p>
  </div>
  <a class="btn-outline" style="left:554px;top:411px;width:119px;height:33px">Read More</a>
</section>

<section class="services">
  <h2>What We Do</h2>
  <div class="svc-img" style="left:88px;top:143px;background:linear-gradient(135deg,#7a4a2a,#b3523a 40%,#3f6a8a 70%,#e8e4d8)" role="img" aria-label="Photo of curved library bookshelves"></div>
  <div class="svc-img" style="left:438px;top:143px;background:linear-gradient(135deg,#dfe3e6,#8b7e74 50%,#c9ced2)" role="img" aria-label="Photo of people discussing around a laptop"></div>
  <div class="svc-img" style="left:787px;top:143px;background:linear-gradient(135deg,#9a958c,#5a4a3e 50%,#cfc8bd)" role="img" aria-label="Photo of a man recording a video lesson"></div>

  <div class="svc-card" style="left:102px;top:324px">
    <h3>Developing Peace<br>Education Curricular</h3>
    <p>Modernizing and internationalizing higher education</p>
    <a class="btn-outline" style="left:24px;top:125px;width:119px;height:33px">Read More</a>
  </div>
  <div class="svc-card" style="left:451px;top:324px">
    <h3>Teaching and<br>Training</h3>
    <p>Utilizing the potential of hybrid learning</p>
    <a class="btn-outline" style="left:24px;top:125px;width:119px;height:33px">Read More</a>
  </div>
  <div class="svc-card" style="left:801px;top:276px">
    <h3>Producing Peace Education Resources</h3>
    <p>Providing engaging and high quality content</p>
    <a class="btn-primary" style="left:24px;top:125px;width:119px;height:33px;font-size:14px;font-weight:400">Read More</a>
  </div>
</section>

<div class="video-band" role="img" aria-label="Photo of historic university city rooftops"></div>
<div class="video-under"></div>
<div class="video-frame" role="img" aria-label="Video illustration of a globe with connected people">
  <svg class="abs" style="left:305px;top:177px" width="90" height="90" viewBox="0 0 90 90">
    <circle cx="45" cy="45" r="44" fill="#8a9aa0" opacity=".8"/>
    <circle cx="45" cy="45" r="35" fill="#0a93e0"/>
    <path d="M38 31 L60 45 L38 59 Z" fill="#fff"/>
  </svg>
</div>

<section class="consortium">
  <h2>Project Consortium</h2>
  <div class="sub">German-Ukrainian Cooperation</div>
  <div class="partner" style="left:89px"><span class="partner-mark"></span>Northvale<br>University<br>Arden</div>
  <div class="partner" style="left:402px"><span class="partner-mark" style="border-radius:0;background:#2b4fa3"></span>Eastmere<br>National<br>Academy</div>
  <div class="partner-cap" style="left:89px">Northvale<br>University Arden</div>
  <div class="partner-cap" style="left:402px">Eastmere National<br>Academy</div>
</section>

<aside class="donor">
  <h2>Donor</h2>
  <div class="donor-card">
    <span class="donor-mark"></span>
    <span class="donor-name">Academic Exchange Fund</span>
  </div>
</aside>

<footer class="site-footer">Copyright © Harbor Lumen. All Rights Reserved</footer>

</body>
</html>
```